Consumer Facing Energy Data Analytics Startup Needs a Postcard to Promote New Product

We need a set of 2 postcards (6 x 4.25 inches as describers in the attached files) to help us promote our product for a new company based in San Francisco called "Lumo Crest".
We develop an alert platform for customers of energy utility companies. Our initial product is "Lumo Notice" - an application that helps people better manage their energy bill by sending an SMS or email alter in advance of a high bill.
We would like to see designs that use the colors blue and orange (same as in the website: www.lumocrest-demo.com). The text of the postcards will be reworked once a layout has been chosen, but we welcome original ways to attract the customers' attention.
Our goal is ultimately to have our targets go the our website and sign up for our service.
The final deliverable should be 8 vector files (preferable .eps, 4 file types, one version in print and one in web format):
- front of card for our small and medium business customers
- front of card for our residential customers
- back of card for our small and medium business customers
- back of card for our residential customers
- DINPro and Avenir

```html
<!DOCTYPE html>
<html lang="en">
<head>
<meta charset="utf-8">
<title>Lumo Crest Postcards</title>
<link rel="stylesheet" href="https://fonts.googleapis.com/css2?family=Barlow:wght@400;500;600;700&family=Noto+Serif:wght@400;700&display=swap">
<style>
  :root {
    --bg: #232323;
    --blue: #1b8fd0;
    --blue-mid: #3aa6dc;
    --blue-dark: #2b86bf;
    --sky-top: #2d8fd6;
    --sky-light: #9fd0f0;
    --orange: #f4a21f;
    --orange-soft: #f6ae3c;
    --white: #ffffff;
    --paper: #f7f7f7;
    --grey-text: #8a8a8a;
    --grey-dark: #555555;
    --grey-line: #cfcfcf;
    --icon-fill: #c9ccd0;
  }
  * { box-sizing: border-box; margin: 0; padding: 0; }
  html, body { width: 1200px; height: 1200px; overflow: hidden; }
  body {
    background: var(--bg);
    font-family: "Barlow", Arial, sans-serif;
    position: relative;
  }

  /* ---------- Back of card ---------- */
  .card-back {
    position: absolute; left: 414px; top: 86px;
    width: 726px; height: 484px;
    background: linear-gradient(180deg, var(--white) 0%, var(--paper) 100%);
  }
  .back-column { position: absolute; left: 14px; top: 0; width: 368px; }
  .back-intro {
    margin-top: 12px; text-align: center;
    color: var(--grey-text); font-size: 20px; line-height: 20px;
  }
  .alert-mock { position: relative; margin-top: 22px; }
  .alert-badge {
    position: absolute; left: 50%; top: -14px; transform: translateX(-50%);
    width: 24px; height: 24px; border-radius: 50%;
    background: var(--orange); border: 2px solid var(--white); z-index: 2;
  }
  .alert-head {
    background: var(--blue-dark); height: 30px;
    display: flex; align-items: center; justify-content: center;
    color: var(--white); font-size: 8px; letter-spacing: 2px; font-weight: 600;
  }
  .alert-body {
    background: var(--blue-mid); height: 83px; text-align: center;
    color: var(--white); font-family: "Noto Serif", Georgia, serif;
    padding-top: 6px;
  }
  .alert-risk { font-size: 8px; opacity: .9; }
  .alert-increase { font-size: 14px; margin-top: 4px; }
  .alert-increase strong { color: var(--orange); font-family: "Barlow", Arial, sans-serif; font-size: 19px; font-weight: 700; }
  .alert-days {
    margin: 8px auto 0; width: 174px; height: 22px; border-radius: 3px;
    background: var(--white); color: var(--grey-dark);
    font-family: "Barlow", Arial, sans-serif; font-size: 7px;
    display: flex; align-items: center; justify-content: center; gap: 4px;
  }
  .alert-days strong { color: var(--orange); font-size: 11px; }
  .tips-title {
    margin-top: 14px; text-align: center; color: var(--grey-dark);
    font-size: 10px; font-weight: 500;
  }
  .tips { display: flex; margin-top: 10px; height: 135px; }
  .tip {
    flex: 1; text-align: center; padding: 0 10px;
    border-right: 1px solid #e4e4e4;
  }
  .tip:last-child { border-right: none; }
  .tip-icon {
    width: 40px; height: 30px; margin: 4px auto 0;
    background: var(--icon-fill); border-radius: 4px;
  }
  .tip-name { margin-top: 12px; font-size: 7px; font-weight: 600; color: var(--grey-dark); }
  .tip-text { margin-top: 5px; font-size: 6px; line-height: 8px; color: var(--grey-text); height: 38px; }
  .tip-button {
    margin: 12px auto 0; width: 58px; height: 14px;
    background: var(--orange); color: var(--white);
    font-size: 6px; font-weight: 600;
    display: flex; align-items: center; justify-content: center;
  }
  .back-divider { margin-top: 2px; height: 2px; background: var(--grey-line); }
  .signup-pill {
    display: inline-flex; align-items: center; justify-content: center;
    background: var(--orange-soft); color: var(--white);
    border-radius: 6px; font-size: 19px; white-space: nowrap;
  }
  .signup-pill strong { font-weight: 600; margin-right: 5px; }
  .back-signup { display: block; width: 290px; height: 28px; margin: 10px auto 0; display: flex; }
  .site-url { color: var(--blue); font-weight: 600; text-align: center; }
  .back-url { margin-top: 6px; font-size: 23px; }
  .stamp-box {
    position: absolute; left: 604px; top: 30px;
    width: 92px; height: 92px; border: 1.5px solid #b8b8b8;
  }

  /* ---------- Front of card ---------- */
  .card-front {
    position: absolute; left: 54px; top: 614px;
    width: 730px; height: 486px; overflow: hidden;
    background: linear-gradient(180deg, #fbfbfb 0%, #eeeeee 100%);
  }
  .hero {
    position: absolute; left: 0; top: 0; width: 730px; height: 342px;
    background: linear-gradient(160deg, var(--sky-top) 0%, #4aa6e2 45%, var(--sky-light) 100%);
  }
  .hero-photo {
    position: absolute; right: 0; top: 0; width: 400px; height: 342px;
    background: linear-gradient(90deg, rgba(170,212,240,0) 0%, rgba(205,228,243,.8) 30%, #dfe9ef 60%, #c7b7a6 100%);
  }
  .hero-accent { position: absolute; left: 0; top: 342px; width: 730px; height: 4px; background: var(--orange); }
  .hero-title {
    position: absolute; left: 14px; top: 50px;
    color: var(--white); font-size: 57px; font-weight: 600; letter-spacing: 1px; line-height: 60px;
  }
  .hero-copy {
    position: absolute; left: 15px; top: 118px; width: 330px;
    color: var(--white); font-size: 18.5px; line-height: 25px;
  }
  .hero-copy p + p { margin-top: 25px; }
  .brand-lockup { position: absolute; left: 18px; top: 388px; display: flex; align-items: center; gap: 16px; }
  .brand-mark { width: 70px; height: 70px; border-radius: 50%; background: var(--orange); }
  .brand-name { color: var(--blue); font-size: 34px; font-weight: 500; letter-spacing: 3px; line-height: 34px; }
  .brand-tagline { color: var(--grey-dark); font-size: 13px; letter-spacing: 1px; margin-top: 4px; }
  .front-divider { position: absolute; left: 402px; top: 376px; width: 1px; height: 95px; background: #bcbcbc; }
  .front-signup { position: absolute; left: 426px; top: 392px; width: 288px; height: 30px; }
  .front-url { position: absolute; left: 414px; top: 430px; width: 310px; font-size: 25px; }
</style>
</head>
<body>

<section class="card-back" aria-label="Postcard back">
  <div class="back-column">
    <p class="back-intro">You will receive on average one email<br>and/or SMS per month, only when<br>Lumo Crest detects for a higher bill</p>

    <div class="alert-mock">
      <span class="alert-badge"></span>
      <div class="alert-head">LUMO NOTICE</div>
      <div class="alert-body">
        <p class="alert-risk">You're at risk of a higher than average energy bill</p>
        <p class="alert-increase">Bill increase from last month: <strong>30%</strong></p>
        <div class="alert-days"><strong>10 days</strong> left in your billing cycle</div>
      </div>
    </div>

    <p class="tips-title">Things you can do right now to lower your risk of high energy bills.</p>

    <div class="tips">
      <div class="tip">
        <div class="tip-icon" role="img" aria-label="Icon of household members"></div>
        <p class="tip-name">Inform the Household</p>
        <p class="tip-text">Let everyone in the home know it is time to save energy this month. Team work pays off!</p>
        <div class="tip-button">I Did It</div>
      </div>
      <div class="tip">
        <div class="tip-icon" role="img" aria-label="Icon of a sleeping laptop"></div>
        <p class="tip-name">Enable Power Save Modes</p>
        <p class="tip-text">Many electronics have power save modes that you can enable to lower costs when they are not in use.</p>
        <div class="tip-button">I Did It</div>
      </div>
      <div class="tip">
        <div class="tip-icon" role="img" aria-label="Icon of a washing machine and thermometer"></div>
        <p class="tip-name">Cold cycle your laundry</p>
        <p class="tip-text">Running your washer on a cold cycle can lower the cost of each load of laundry.</p>
        <div class="tip-button">I Did It</div>
      </div>
    </div>

    <div class="back-divider"></div>
    <div class="signup-pill back-signup"><strong>Sign Up</strong> for Lumo Notice Today!</div>
    <p class="site-url back-url">www.lumocrest-demo.com</p>
  </div>
  <div class="stamp-box"></div>
</section>

<section class="card-front" aria-label="Postcard front">
  <div class="hero"></div>
  <div class="hero-photo" role="img" aria-label="Photo of a woman working on a laptop by a bright window with sky behind"></div>
  <div class="hero-accent"></div>
  <h1 class="hero-title">LUMO CREST</h1>
  <div class="hero-copy">
    <p>Lumo Notice is a web application that puts you in control of your utility bill and energy usage.</p>
    <p>Everyday, Lumo Crest will analyze your energy usage.</p>
  </div>

  <div class="brand-lockup">
    <span class="brand-mark"></span>
    <div>
      <p class="brand-name">LUMO CREST</p>
      <p class="brand-tagline">ENERGY ANALYTICS AND INSIGHTS</p>
    </div>
  </div>
  <div class="front-divider"></div>
  <div class="signup-pill front-signup"><strong>Sign Up</strong> for Lumo Notice Today!</div>
  <p class="site-url front-url">www.lumocrest-demo.com</p>
</section>

</body>
</html>
```